Create a new website for "The Galleria at Briar Ridge"

I need a website for a shopping center in Atlanta USA. I want a classy high end look with high end motion videos (which I will provide).
The purpose of website is to attract new tenants to fill up vacant office spaces we have.
we will highlight existing cool stores and advertise that this is a cool place to start a new tenants business or office . ideally IT businesses in Alpharetta city in Georgia state in USA

Target Market(s)

commercial office tenants

Industry/Entity Type

Real Estate

Contact Information for Business Card

classy high end design
Galleria at Briar Ridge
address:
2870 Briar Ridge Pkwy
Alpharetta GA 30005

Logo Text

I am open. Anything that attracts new IT tech tenants to lease up shopping center/ office space

Coding

Coded - Design and coding required

Number of Pages Required

5+ page

Requirements
Must have
• easy to browse

here is a link to some photos. i will provide videos shortly

http://www.pelurano.com/2014/04/Building-Photos-3/n-7Q4hk/
Nice to have
• please look at some of mall websites i like. Moving videos and images on home page

I really like this one: https://www.plazaatcrestvane.com/

others are

https://belmorecourt.com/

https://www.visitquorrelbay.com/

```html
<!DOCTYPE html>
<html lang="en">
<head>
<meta charset="utf-8">
<title>The Galleria at Briar Ridge</title>
<link href="https://fonts.googleapis.com/css2?family=Poppins:wght@400;500;600;700&family=Libre+Baskerville:wght@700&display=swap" rel="stylesheet">
<style>
:root{
  --black:#0b0b0b;
  --ink:#1a1a1a;
  --nav:#111111;
  --dark:#2b2b2b;
  --white:#ffffff;
  --line:#dcdcdc;
  --muted:#555555;
  --soft:#f6f6f6;
}
*{box-sizing:border-box;margin:0;padding:0}
html,body{width:1200px;height:4005px;overflow:hidden}
body{position:relative;font-family:'Poppins',sans-serif;color:var(--ink);background:var(--white)}
.abs{position:absolute}
a{color:inherit;text-decoration:none}

/* header */
.topbar{left:0;top:0;width:1200px;height:62px;background:var(--white)}
.call{left:143px;top:14px;display:flex;gap:10px;align-items:center}
.call small{display:block;font-size:11px;line-height:13px}
.call strong{display:block;font-size:12px;font-weight:600}
.brand{left:0;width:1200px;top:15px;text-align:center;font-family:'Libre Baskerville',serif;font-weight:700;font-size:24px;letter-spacing:.3px}
.lang{left:962px;top:17px;width:82px;height:31px;border:1px solid #999;font-size:13px;font-weight:600;display:flex;align-items:center;justify-content:space-between;padding:0 14px}
.mainnav{left:0;top:62px;width:1200px;height:52px;background:var(--nav);display:flex;justify-content:center;align-items:center;gap:0}
.mainnav a{color:var(--white);font-size:12px;font-weight:600;padding:0 22px;position:relative}
.mainnav a+a::before{content:"";position:absolute;left:-4px;top:-4px;width:1px;height:22px;background:#777;transform:rotate(20deg)}

/* hero */
.hero{left:0;top:114px;width:1200px;height:646px;background:linear-gradient(180deg,#8a94a0 0%,#a8aaa6 30%,#8e8a80 60%,#5e5a52 85%,#4a4a48 100%)}
.hero-title{left:0;width:1200px;top:300px;text-align:center;color:var(--white);font-weight:700}
.hero-title .l1{font-size:55px;line-height:64px;display:block}
.hero-title .l2{font-size:83px;line-height:92px;display:block;letter-spacing:-1px}
.btn-start{left:517px;top:506px;width:165px;height:44px;border-radius:22px;background:var(--white);font-size:14px;font-weight:600;display:flex;align-items:center;justify-content:center}

/* section titles */
.sec-title{display:flex;align-items:center;gap:16px;font-weight:700;letter-spacing:-.5px}
.sec-rule{height:3px;width:60px}

/* trending */
.trend-bg{left:0;top:808px;width:645px;height:515px;background:var(--soft)}
.trend-bg2{left:825px;top:960px;width:315px;height:190px;background:#f9f9f9}
.card{border:1px solid var(--line);background:var(--white)}
.prod{border-radius:6px}
.coll small{display:block;font-size:11px;font-weight:400}
.coll b{display:block;font-weight:600}
.shop{display:inline-flex;align-items:center;justify-content:center;border:1.5px solid var(--ink);font-weight:500}

/* films */
.films{left:0;top:1476px;width:1200px;height:636px;background:var(--dark)}
.video{top:1681px;height:296px}
.play{width:44px;height:44px;border-radius:50%;background:rgba(255,255,255,.7);display:flex;align-items:center;justify-content:center}
.dot{top:2017px;width:11px;height:11px;border-radius:50%;background:#888}

/* blog */
.post{top:2301px;width:280px;height:476px;border:1px solid var(--line);background:var(--white)}
.post .pic{position:absolute;left:0;top:0;width:278px;height:263px}
.post .date{position:absolute;left:100px;top:224px;width:78px;height:78px;border-radius:50%;background:var(--ink);color:var(--white);text-align:center;font-size:15px;line-height:20px;padding-top:18px;font-weight:500}
.post .date b{font-size:22px;font-weight:600;display:block;line-height:22px}
.post h3{position:absolute;left:10px;width:258px;top:322px;text-align:center;font-size:14px;font-weight:600;line-height:16px}
.post p{position:absolute;left:18px;width:242px;top:365px;text-align:center;font-size:13px;line-height:17px;color:var(--muted)}
.post .more{position:absolute;left:0;width:278px;top:440px;text-align:center;font-size:10px;font-weight:700}
.btn-more{left:486px;top:2810px;width:227px;height:39px;border:2px solid var(--ink);font-size:11px;font-weight:700;letter-spacing:1px;display:flex;align-items:center;justify-content:center}

/* join */
.join{left:0;top:2942px;width:1200px;height:566px;background:linear-gradient(90deg,#5a3a20 0%,#7a5030 30%,#4a3526 55%,#6a5848 80%,#3f3328 100%)}
.field{background:var(--white);font-size:12px;color:#333;padding:0 16px;display:flex;align-items:center}
.submit{left:524px;top:3411px;width:152px;height:42px;border:2px solid var(--white);color:var(--white);font-size:17px;font-weight:500;display:flex;align-items:center;justify-content:center}

/* footer */
.footer{left:0;top:3508px;width:1200px;height:497px;background:var(--black)}
.cbox{top:3571px;height:106px;border:1px solid #333;display:flex;align-items:center;gap:14px;padding-left:32px;color:var(--white);font-size:12px}
.cbox b{display:block;font-size:13px;font-weight:600}
.cicon{width:40px;height:36px;background:var(--white);border-radius:2px;display:flex;align-items:center;justify-content:center;flex:none}
.fnav{left:0;width:1200px;top:3826px;display:flex;justify-content:center;gap:0;color:var(--white);font-size:12px;font-weight:600}
.fnav a{padding:0 22px}
.fnav a.on{border-bottom:2px solid var(--white);padding-bottom:8px;margin:0 22px;padding-left:0;padding-right:0}
.social{top:3865px;width:25px;height:25px;border:1.5px solid var(--white);border-radius:50%}
</style>
</head>
<body>

<header>
  <div class="abs topbar"></div>
  <div class="abs call">
    <svg width="20" height="20" viewBox="0 0 24 24"><path d="M6.6 10.8c1.4 2.8 3.8 5.1 6.6 6.6l2.2-2.2c.3-.3.7-.4 1-.2 1.1.4 2.3.6 3.6.6.6 0 1 .4 1 1V20c0 .6-.4 1-1 1C10.6 21 3 13.4 3 4c0-.6.4-1 1-1h3.5c.6 0 1 .4 1 1 0 1.3.2 2.5.6 3.6.1.3 0 .7-.2 1z" fill="#111"/></svg>
    <div><small>CALL US:</small><strong>(123) 456 7890</strong></div>
  </div>
  <div class="abs brand">THE GALLERIA AT BRIAR RIDGE</div>
  <div class="abs lang">Eng <svg width="10" height="7" viewBox="0 0 10 7"><path d="M1 1l4 4 4-4" stroke="#111" fill="none" stroke-width="1.5"/></svg></div>
  <nav class="abs mainnav">
    <a>HOME</a><a>TRENDING NOW</a><a>FILM</a><a>DIRECTORY</a><a>HAPPENING NOW</a><a>BLOG</a><a>CONTACT</a>
  </nav>
</header>

<section>
  <div class="abs hero" role="img" aria-label="Photo of the shopping center building with storefronts, columns and young trees"></div>
  <h1 class="abs hero-title"><span class="l1">THE GALLERIA</span><span class="l2">AT BRIAR RIDGE</span></h1>
  <a class="abs btn-start">GET STARTED</a>
</section>

<section>
  <div class="abs trend-bg"></div>
  <div class="abs trend-bg2"></div>
  <div class="abs sec-title" style="left:535px;top:895px;font-size:50px">
    <svg width="20" height="16" viewBox="0 0 20 16"><path d="M10 0v16L0 8zM20 0v16L10 8z" fill="#111"/></svg>
    TRENDING NOW
    <svg width="20" height="16" viewBox="0 0 20 16"><path d="M0 0v16l10-8zM10 0v16l10-8z" fill="#111"/></svg>
  </div>
  <div class="abs sec-rule" style="left:738px;top:962px;background:#111"></div>

  <div class="abs card" style="left:143px;top:959px;width:320px;height:422px"></div>
  <div class="abs prod" style="left:182px;top:909px;width:240px;height:320px;background:linear-gradient(180deg,#2c3a55 0%,#1e2430 35%,#3a3a3a 50%,#222 100%)" role="img" aria-label="Open laptop seen from above"></div>
  <div class="abs coll" style="left:143px;top:1252px;width:320px;text-align:center">
    <small style="font-size:14px">LOREM IPSUM DOLOR</small>
    <b style="font-size:28px;line-height:38px">COLLECTION</b>
  </div>
  <a class="abs shop" style="left:252px;top:1320px;width:109px;height:32px;font-size:12px">SHOP NOW</a>

  <div class="abs card" style="left:480px;top:1044px;width:272px;height:113px"></div>
  <div class="abs coll" style="left:496px;top:1066px"><small>LOREM IPSUM DOLOR</small><b style="font-size:20px;line-height:28px">COLLECTION</b></div>
  <a class="abs shop" style="left:498px;top:1116px;width:78px;height:23px;font-size:9px">SHOP NOW</a>
  <div class="abs prod" style="left:640px;top:1016px;width:92px;height:130px;background:linear-gradient(135deg,#3a3a3a 0%,#6a6a6a 45%,#c6a6e6 60%,#8a5ad0 100%)" role="img" aria-label="Two smartphones standing side by side"></div>

  <div class="abs card" style="left:771px;top:1044px;width:272px;height:113px"></div>
  <div class="abs coll" style="left:782px;top:1062px"><small>LOREM IPSUM DOLOR</small><b style="font-size:20px;line-height:28px">COLLECTION</b></div>
  <a class="abs shop" style="left:786px;top:1114px;width:78px;height:23px;font-size:9px">SHOP NOW</a>
  <div class="abs prod" style="left:927px;top:1016px;width:104px;height:130px;background:linear-gradient(135deg,#2a2a2a 0%,#e64a7a 40%,#f09a4a 65%,#3a3a3a 100%)" role="img" aria-label="Tablet computer with colorful screen"></div>

  <div class="abs card" style="left:480px;top:1214px;width:565px;height:165px"></div>
  <div class="abs coll" style="left:520px;top:1248px"><small style="font-size:14px">LOREM IPSUM DOLOR</small><b style="font-size:28px;line-height:38px">COLLECTION</b></div>
  <a class="abs shop" style="left:522px;top:1318px;width:110px;height:31px;font-size:12px">SHOP NOW</a>
  <div class="abs prod" style="left:772px;top:1180px;width:210px;height:195px;border-radius:50% 50% 20% 20%;background:radial-gradient(circle at 50% 60%,#6a6a6a 0%,#2a2a2a 60%,#111 100%)" role="img" aria-label="Over-ear headphones"></div>
</section>

<section>
  <div class="abs films"></div>
  <div class="abs sec-title" style="left:347px;top:1555px;font-size:50px;color:#fff">
    <svg width="20" height="16" viewBox="0 0 20 16"><path d="M10 0v16L0 8zM20 0v16L10 8z" fill="#fff"/></svg>
    <span style="margin:0 18px">VIEW OUR FILMS</span>
    <svg width="20" height="16" viewBox="0 0 20 16"><path d="M0 0v16l10-8zM10 0v16l10-8z" fill="#fff"/></svg>
  </div>
  <div class="abs sec-rule" style="left:564px;top:1619px;background:#fff"></div>

  <div class="abs video" style="left:143px;width:285px;border:3px solid #fff;background:linear-gradient(135deg,#3a4250 0%,#7a6050 45%,#3a4656 100%)" role="img" aria-label="Video still of a woman with headphones holding a phone"></div>
  <div class="abs play" style="left:263px;top:1807px;background:#fff"><svg width="14" height="16" viewBox="0 0 14 16"><path d="M0 0l14 8-14 8z" fill="#222"/></svg></div>
  <svg class="abs" style="left:386px;top:1710px" width="16" height="14" viewBox="0 0 16 14"><path d="M8 14L1.5 7.5A4 4 0 018 2a4 4 0 016.5 5.5z" fill="#fff"/></svg>
  <svg class="abs" style="left:388px;top:1742px" width="12" height="12" viewBox="0 0 12 12"><path d="M2 2l6 4-6 4" stroke="#fff" fill="none" stroke-width="1.5"/></svg>

  <div class="abs video" style="left:451px;width:286px;background:linear-gradient(135deg,#8a9a6a 0%,#5a8a4a 45%,#c8b8a0 100%)" role="img" aria-label="Video still of a young man in a green sweater using a tablet"></div>
  <div class="abs play" style="left:572px;top:1807px"><svg width="14" height="16" viewBox="0 0 14 16"><path d="M0 0l14 8-14 8z" fill="#444"/></svg></div>

  <div class="abs video" style="left:757px;width:286px;background:linear-gradient(135deg,#6a6a5a 0%,#a0a8b8 50%,#7a7a88 100%)" role="img" aria-label="Video still of a woman on a sofa looking at her phone"></div>
  <div class="abs play" style="left:878px;top:1807px"><svg width="14" height="16" viewBox="0 0 14 16"><path d="M0 0l14 8-14 8z" fill="#444"/></svg></div>

  <div class="abs dot" style="left:556px"></div>
  <div class="abs dot" style="left:577px;background:#fff"></div>
  <div class="abs dot" style="left:598px"></div>
  <div class="abs dot" style="left:620px"></div>
</section>

<section>
  <div class="abs sec-title" style="left:490px;top:2204px;font-size:50px">
    <svg width="20" height="16" viewBox="0 0 20 16"><path d="M10 0v16L0 8zM20 0v16L10 8z" fill="#111"/></svg>
    BLOG
    <svg width="20" height="16" viewBox="0 0 20 16"><path d="M0 0v16l10-8zM10 0v16l10-8z" fill="#111"/></svg>
  </div>
  <div class="abs sec-rule" style="left:570px;top:2266px;background:#111"></div>

  <article class="abs post" style="left:143px">
    <div class="pic" style="background:linear-gradient(135deg,#8a8a80 0%,#6a5a50 50%,#c0b8b0 100%)" role="img" aria-label="Two colleagues looking at a tablet outdoors"></div>
    <div class="date"><b>17</b>MAR</div>
    <h3>LOREM IPSUM DOLOR SIT AMET, CONSECTETUR</h3>
    <p>Lorem ipsum dolor sit amet, con-sectetur adipiscing elit, sed do eiusmod tempor incididunt ut</p>
    <div class="more">READ MORE »</div>
  </article>
  <article class="abs post" style="left:452px">
    <div class="pic" style="background:linear-gradient(135deg,#7a9a5a 0%,#a8a078 50%,#5a6a4a 100%)" role="img" aria-label="Couple working together on a laptop on the grass"></div>
    <div class="date"><b>18</b>MAR</div>
    <h3>LOREM IPSUM DOLOR SIT AMET, CONSECTETUR</h3>
    <p>Lorem ipsum dolor sit amet, con-sectetur adipiscing elit, sed do eiusmod tempor incididunt ut</p>
    <div class="more">READ MORE »</div>
  </article>
  <article class="abs post" style="left:763px">
    <div class="pic" style="background:linear-gradient(135deg,#4a6a90 0%,#2a4a7a 50%,#5a4038 100%)" role="img" aria-label="Man in a denim shirt using a smartphone"></div>
    <div class="date"><b>19</b>MAR</div>
    <h3>LOREM IPSUM DOLOR SIT AMET, CONSECTETUR</h3>
    <p>Lorem ipsum dolor sit amet, con-sectetur adipiscing elit, sed do eiusmod tempor incididunt ut</p>
    <div class="more">READ MORE »</div>
  </article>
  <a class="abs btn-more">VIEW MORE OF MY POSTS</a>
</section>

<section>
  <div class="abs join" role="img" aria-label="Empty interior space with polished floor and large windows"></div>
  <div class="abs sec-title" style="left:382px;top:3030px;font-size:50px;color:#fff">
    <svg width="20" height="16" viewBox="0 0 20 16"><path d="M10 0v16L0 8zM20 0v16L10 8z" fill="#fff"/></svg>
    JOIN THE LIST
    <svg width="20" height="16" viewBox="0 0 20 16"><path d="M0 0v16l10-8zM10 0v16l10-8z" fill="#fff"/></svg>
  </div>
  <div class="abs sec-rule" style="left:564px;top:3094px;background:#fff"></div>
  <div class="abs field" style="left:339px;top:3124px;width:250px;height:40px">Name</div>
  <div class="abs field" style="left:600px;top:3124px;width:253px;height:40px">E-Mail</div>
  <div class="abs" style="left:612px;top:3182px;font-size:12px;color:#fff">Language (Select One) *</div>
  <div class="abs field" style="left:339px;top:3212px;width:250px;height:40px">Phone</div>
  <div class="abs field" style="left:600px;top:3212px;width:253px;height:40px;justify-content:space-between">English <svg width="10" height="8" viewBox="0 0 10 8"><path d="M0 0h10L5 8z" fill="#111"/></svg></div>
  <div class="abs field" style="left:339px;top:3277px;width:511px;height:109px;align-items:flex-start;padding-top:14px">Message</div>
  <a class="abs submit">SUBMIT</a>
</section>

<footer>
  <div class="abs footer"></div>
  <div class="abs cbox" style="left:143px;width:200px">
    <div class="cicon"><svg width="20" height="20" viewBox="0 0 24 24"><path d="M6.6 10.8c1.4 2.8 3.8 5.1 6.6 6.6l2.2-2.2c.3-.3.7-.4 1-.2 1.1.4 2.3.6 3.6.6.6 0 1 .4 1 1V20c0 .6-.4 1-1 1C10.6 21 3 13.4 3 4c0-.6.4-1 1-1h3.5c.6 0 1 .4 1 1 0 1.3.2 2.5.6 3.6.1.3 0 .7-.2 1z" fill="none" stroke="#111" stroke-width="1.6"/></svg></div>
    <div><b>Phone:</b>123-456-7890</div>
  </div>
  <div class="abs cbox" style="left:435px;width:261px;align-items:flex-start;padding-top:26px">
    <div class="cicon"><svg width="16" height="20" viewBox="0 0 16 20"><path d="M8 19s-6-6.5-6-11a6 6 0 0112 0c0 4.5-6 11-6 11z" fill="none" stroke="#111" stroke-width="1.6"/><circle cx="8" cy="8" r="2.2" fill="#111"/></svg></div>
    <div><b>Address:</b>Lorem ipsum Public 1234,<br>Somestreet NY 0123</div>
  </div>
  <div class="abs cbox" style="left:788px;width:256px">
    <div class="cicon"><svg width="22" height="16" viewBox="0 0 22 16"><rect x="1" y="1" width="20" height="14" fill="none" stroke="#111" stroke-width="1.6"/><path d="M1 1l10 8 10-8" fill="none" stroke="#111" stroke-width="1.6"/></svg></div>
    <div><b>Mail:</b>info@briarridgemail.com</div>
  </div>
  <div class="abs" style="left:0;width:1200px;top:3720px;text-align:center;color:#fff;font-family:'Libre Baskerville',serif;font-weight:700;font-size:19px">THE GALLERIA AT BRIAR RIDGE</div>
  <div class="abs" style="left:340px;width:520px;top:3770px;text-align:center;color:#fff;font-size:11.5px;line-height:19px">Lorem ipsum dolor sit amet, consectetur adipiscing elit, sed do eiusmod tempor incididunt ut labore et dolore magna aliqua.</div>
  <nav class="abs fnav">
    <a class="on">HOME</a><a>TRENDING NOW</a><a>FILM</a><a>DIRECTORY</a><a>HAPPENING NOW</a><a>BLOG</a><a>CONTACT</a>
  </nav>
  <div class="abs social" style="left:540px"></div>
  <div class="abs social" style="left:580px"></div>
  <div class="abs social" style="left:618px"></div>
  <div class="abs" style="left:0;top:3955px;width:1200px;height:1px;background:#333"></div>
  <div class="abs" style="left:0;width:1200px;top:3972px;text-align:center;color:#888;font-size:12px">© Copyright 2020 &nbsp; THE GALLERIA AT BRIAR RIDGE. All Rights Reserved</div>
</footer>

</body>
</html>
```